Occupational Therapist does home accessibility for disabled folks; needs business card design

We need a business card for a company in Portland, Oregon that specializes in making homes accessible, comfortable, and functional for people who are disabled or aging who would like to stay in THEIR home. Our medical background as Occupational Therapists allows us to translate the functional needs of the person into the recommendations for the design of the home remodel.

Target Market(s)

Elderly, children of elderly
People with disabilities, families of people with disabilities

Industry/Entity Type

Business

Contact Information for Business Card

Company name: HomeWise
Name: Danielle Reyes Crawford, OTR/L, CAPS, ECHM
Occupational Therapist, Home Modification & Accessibility Specialist
website: www.homewiseforyears.com
email: homewiseforyears@nestmail.example
phone: (503)218-4057
CCB #: 487315

Font styles to use
Sans Serif

Requirements
Must have
• My logo
• Easy to read font with contrasting background
• Please list the Services offered: Occupational Therapy, Home safety & accessibility assessments, Home modification consulting, project management
Nice to have
• Friendly, welcoming feel
Should not have
• Dark colored background

```html
<!DOCTYPE html>
<html lang="en">
<head>
<meta charset="utf-8">
<title>HomeWise business cards</title>
<link rel="stylesheet" href="https://fonts.googleapis.com/css2?family=Open+Sans:wght@400;600;700&display=swap">
<style>
  :root {
    --orange: #d68a14;
    --grey: #595959;
    --grey-dark: #4a4a4a;
    --card: #fbfbf9;
    --backdrop: #ece6dd;
  }
  * { box-sizing: border-box; margin: 0; padding: 0; }
  html, body { width: 1200px; height: 800px; overflow: hidden; }
  body {
    background: var(--backdrop);
    font-family: "Open Sans", Arial, sans-serif;
    color: var(--grey);
    position: relative;
  }
  .card {
    position: absolute;
    left: 320px;
    width: 560px;
    height: 320px;
    background: var(--card);
    box-shadow: 0 6px 18px rgba(0,0,0,0.12);
    overflow: hidden;
  }
  .card--services { top: 50px; }
  .card--contact { top: 420px; }

  .brand {
    display: flex;
    align-items: center;
    gap: 10px;
    color: var(--orange);
    font-weight: 700;
    line-height: 1;
  }
  .brand__square {
    width: 22px; height: 22px;
    background: var(--orange);
  }

  /* Services face */
  .card--services .brand {
    position: absolute;
    top: 78px; left: 0; right: 0;
    justify-content: center;
    font-size: 52px;
  }
  .card--services .brand__square { width: 30px; height: 30px; }
  .services__title {
    position: absolute;
    top: 168px; left: 0; right: 0;
    text-align: center;
    color: var(--orange);
    font-weight: 700;
    font-size: 20px;
  }
  .services__list {
    position: absolute;
    top: 204px; left: 0; right: 0;
    text-align: center;
    font-size: 15px;
    line-height: 1.45;
    color: var(--grey);
  }

  /* Contact face */
  .contact__band {
    position: absolute;
    top: 0; left: 0;
    width: 100%; height: 74px;
    background: var(--orange);
  }
  .card--contact .brand {
    position: absolute;
    top: 104px; right: 36px;
    font-size: 38px;
  }
  .person {
    position: absolute;
    top: 108px; left: 30px;
    width: 220px;
  }
  .person__name {
    color: var(--orange);
    font-weight: 700;
    font-size: 19px;
    line-height: 1.2;
  }
  .person__credentials {
    color: var(--orange);
    font-weight: 600;
    font-size: 14px;
    margin-top: 3px;
  }
  .person__role {
    margin-top: 10px;
    font-size: 14px;
    line-height: 1.35;
    color: var(--grey);
  }
  .contact__divider {
    position: absolute;
    top: 196px; left: 262px;
    width: 2px; height: 84px;
    background: var(--orange);
  }
  .contact__list {
    position: absolute;
    top: 196px; left: 280px;
    list-style: none;
    font-size: 13.5px;
    line-height: 1.55;
    color: var(--grey-dark);
  }
  .contact__item { display: flex; align-items: center; gap: 7px; }
  .contact__item svg { width: 13px; height: 13px; fill: var(--orange); flex: none; }
  .contact__item--plain { padding-left: 0; }
</style>
</head>
<body>

  <section class="card card--services" aria-label="Card front: services">
    <div class="brand"><span class="brand__square"></span><span class="brand__name">HomeWise</span></div>
    <h2 class="services__title">Services</h2>
    <p class="services__list">
      Occupational Therapy | Home safety &amp; accessibility assessments<br>
      Home modification consulting | project management
    </p>
  </section>

  <section class="card card--contact" aria-label="Card back: contact details">
    <div class="contact__band"></div>
    <div class="brand"><span class="brand__square"></span><span class="brand__name">HomeWise</span></div>

    <div class="person">
      <h1 class="person__name">Danielle Reyes Crawford</h1>
      <p class="person__credentials">OTR/L, CAPS, ECHM</p>
      <p class="person__role">Occupational Therapist,<br>Home Modification &amp;<br>Accessibility Specialist</p>
    </div>

    <div class="contact__divider"></div>

    <ul class="contact__list">
      <li class="contact__item">
        <svg viewBox="0 0 24 24" aria-hidden="true"><path d="M6.6 10.8a15.1 15.1 0 0 0 6.6 6.6l2.2-2.2c.3-.3.7-.4 1-.2 1.1.4 2.3.6 3.6.6.6 0 1 .4 1 1V20c0 .6-.4 1-1 1A17 17 0 0 1 3 4c0-.6.4-1 1-1h3.5c.6 0 1 .4 1 1 0 1.3.2 2.5.6 3.6.1.3 0 .7-.2 1z"/></svg>
        (503)218-4057
      </li>
      <li class="contact__item">
        <svg viewBox="0 0 24 24" aria-hidden="true"><path d="M2 5h20v14H2z M3.5 6.5 12 13l8.5-6.5" stroke="#fbfbf9" stroke-width="1.4"/></svg>
        homewiseforyears@nestmail.example
      </li>
      <li class="contact__item">
        <svg viewBox="0 0 24 24" aria-hidden="true"><circle cx="12" cy="12" r="10"/><path d="M2 12h20M12 2c3 3 3 17 0 20M12 2c-3 3-3 17 0 20" stroke="#fbfbf9" stroke-width="1.4" fill="none"/></svg>
        www.homewiseforyears.com
      </li>
      <li class="contact__item contact__item--plain">CCB #: 487315</li>
    </ul>
  </section>

</body>
</html>
```